Healing Arts Brochure with Simple, Elegant, Zen Design ,

I need to create a brochure for an upcoming event and I have to complete this project in the next few days.
I would like a tri-fold or z fold type of brochure- standard size of 8.5 x 11- both sides with text

i would like the overall design to be simple, elegant and zen .... yet not too plain :-))
I would like the fonts used to be clean and clear and ... easy to read.
I would like the background color to be white/cream or light color
Please do not use too many colors when working with the descriptions of my services or break those sections up too much ... a little is ok.
I don't want the brochure to be busy

I've uploaded the text, my photo, a photo that I will be using on my website, my logo symbol without my name and several logo symbols with my name in different font styles. I am not wed to any of the various font styles of the logo just yet.
TEXT FILE IS UPLOADED

Dear Designers, The design submissions that I'm receiving so far have not been including all 3 pages of text in the brochure. I pulled my text file to update it with the instructions that there are 3 pages of text information that need to be on the brochure. Unfortunately, I'm not able to upload the text file - seems to be a glitch on the ArtMarkly website.. I called for support and they won't get back to me for a couple of hours. That will be around 11:00 am PST in the USA. PLEASE CHECK BACK if you haven't already downloaded the text file. Otherwise, please add the missing information and resubmit your ideas. Thank you!! MR

Target Market(s)

My services target clients in the healing arts.

Industry/Entity Type

Event

Requirements
Must have
• Please include the colors tones of my logo and the sunset photo -golds, oranges, blues
Brochure must include my photo and the sunset photo
Should not have
• Objects like teacups etc. that have nothing to do with my services - thank you kindly
I don't want any other photos or objects on the brochure other than my photo and the sun
Please don't put the tagline in quotes
Please do not make the brochure busy with too many colors in the text.

```html
<!DOCTYPE html>
<html lang="en">
<head>
<meta charset="utf-8">
<title>Mira Rowan – Sound Therapy Brochure</title>
<link href="https://fonts.googleapis.com/css2?family=Fira+Sans:wght@300;400;600&display=swap" rel="stylesheet">
<style>
  :root {
    --paper: #ffffff;
    --ink: #1c1c1c;
    --muted: #6f6f6f;
    --brand-blue: #3f6cb4;
    --sun-gold: #f6b335;
    --sun-orange: #ec8a1f;
    --deep-orange: #e07020;
    --band-black: #000000;
  }
  * { margin: 0; padding: 0; box-sizing: border-box; }
  html, body { width: 1200px; height: 1000px; overflow: hidden; background: var(--paper); }
  body { font-family: "Fira Sans", Arial, sans-serif; color: var(--ink); position: relative; }

  .sheet {
    position: absolute; left: 26px; top: 57px; width: 1150px; height: 887px;
    border: 1px solid var(--ink); background: var(--paper); overflow: hidden;
  }
  .panel { position: absolute; top: 0; height: 100%; }
  .panel--inner { left: 0; width: 380px; }
  .panel--back { left: 380px; width: 380px; }
  .panel--cover { left: 760px; width: 390px; }

  /* Left panel */
  .section-tab {
    position: absolute; left: 36px; top: 42px; width: 206px; height: 44px;
    background: linear-gradient(180deg, #f7a23a 0%, #fbd27a 45%, #f59a2c 100%);
    font-weight: 600; font-size: 18px; line-height: 44px; padding-left: 16px; color: var(--ink);
  }
  .section-tab::after {
    content: ""; position: absolute; left: 172px; bottom: -8px;
    border-left: 6px solid transparent; border-right: 6px solid transparent;
    border-top: 8px solid var(--sun-orange);
  }
  .body-copy {
    position: absolute; left: 52px; top: 113px; width: 277px;
    font-weight: 300; font-size: 15.4px; line-height: 19.2px; text-align: justify; hyphens: auto;
  }
  .body-copy p { text-indent: 50px; margin-bottom: 19.2px; }
  .ornament-block {
    position: absolute; left: 0; bottom: 0; width: 380px; height: 244px;
    background: radial-gradient(circle at 45% 40%, #fbd9b0 0%, #f4a347 35%, #e8861f 100%);
  }

  /* Middle panel */
  .brand {
    position: absolute; display: flex; align-items: center; gap: 10px;
    color: var(--brand-blue); font-weight: 400;
  }
  .brand-dot { border-radius: 50%; background: var(--sun-orange); flex: none; }
  .brand--back { left: 66px; top: 642px; font-size: 30px; }
  .brand--back .brand-dot { width: 34px; height: 34px; }
  .rule { position: absolute; left: 74px; top: 742px; width: 252px; border-top: 1px solid var(--ink); }
  .contact {
    position: absolute; left: 0; width: 380px; top: 762px; text-align: center;
    font-size: 16.5px; line-height: 20.8px; font-weight: 400;
  }

  /* Right panel */
  .sunset-photo {
    position: absolute; left: 0; top: 0; width: 390px; height: 223px;
    background:
      radial-gradient(circle at 52% 34%, #fffbe0 0%, #ffe27a 8%, #f9b53a 28%, transparent 60%),
      linear-gradient(180deg, #e7901f 0%, #f3a93a 45%, #f6b94a 55%, #d9781a 100%);
  }
  .pointer-down {
    position: absolute; left: 302px; top: 223px;
    border-left: 10px solid transparent; border-right: 10px solid transparent;
    border-top: 22px solid var(--deep-orange);
  }
  .brand--cover { left: 58px; top: 262px; font-size: 36px; }
  .brand--cover .brand-dot { width: 42px; height: 42px; }
  .tagline {
    position: absolute; left: 0; width: 418px; top: 356px; text-align: center;
    font-weight: 300; font-size: 17px; line-height: 21px; color: var(--muted);
  }
  .cover-web { position: absolute; left: 152px; top: 763px; font-size: 13px; }
  .footer-band {
    position: absolute; left: 0; bottom: 0; width: 390px; height: 58px; background: var(--band-black);
  }
  .pointer-up {
    position: absolute; left: 304px; bottom: 58px;
    border-left: 13px solid transparent; border-right: 13px solid transparent;
    border-bottom: 22px solid var(--band-black);
  }
</style>
</head>
<body>
  <main class="sheet">
    <section class="panel panel--inner">
      <h2 class="section-tab">Sound Therapy</h2>
      <div class="body-copy">
        <p>For thousands of years cultures throughout the world have used sound for healing, cultivating resiliency and for affirming spiritual connection. Scientific research in the fields of medicine and psychology has affirmed the therapeutic effect of sound for rebalancing, restoring and re-energizing both the body and the psyche.</p>
        <p>The use of sound therapy can be a highly effective way to support healing and enhance overall wellness. Every organism in our universe has its own resonant frequencies. My specialty is working with singing bowls, gongs or tuning forks to assist in the attunement of energy flows in the body. This approach works on physical, emotional and mental levels to facilitate stress-reduction, restore health and promote well-being. Many of my clients enjoy the use of sound therapy as an adjunct part of their Body Listening™, DeepRest® or Yoga Nidra sessions.</p>
      </div>
      <div class="ornament-block" role="img" aria-label="Warm orange textured block with a white lotus flower ornament"></div>
    </section>

    <section class="panel panel--back">
      <div class="brand brand--back"><span class="brand-dot"></span><span>Mira Rowan</span></div>
      <div class="rule"></div>
      <address class="contact" style="font-style:normal">
        For more information:<br>
        www.mirarowan.com<br>
        mira@mirarowan.com<br>
        415-555-0142
      </address>
    </section>

    <section class="panel panel--cover">
      <div class="sunset-photo" role="img" aria-label="Photograph of a golden sunset over calm water"></div>
      <div class="pointer-down"></div>
      <h1 class="brand brand--cover"><span class="brand-dot"></span><span>Mira Rowan</span></h1>
      <p class="tagline">Offerings to support you<br>in discovering health, resiliency<br>and well-being.</p>
      <p class="cover-web">www.mirarowan.com</p>
      <div class="pointer-up"></div>
      <div class="footer-band"></div>
    </section>
  </main>
</body>
</html>
```